Shift Haven Brochure for on call home care staffing

Brochure to describe Shift haven services. Shift haven provides after hours on-call staffing and scheduling only for home care agencies. We are 100% US Based with real agents in person answering calls. We act as an extension of their agency and integrate seamlessly. I dropped in my attempt at the brochure but my AI images suck. We want realistic images with an Americana feel. I also don't want the gold color or the same images on the new one. Feel free to redo the writing.

Target Market(s)

home care agencies

Industry/Entity Type

Health care staffing

Font styles to use
Serif
Sans Serif

Colors
0054AA
0677BA
7BADD7
CADEEF
E8F1F8

Requirements
Must have
• Catchy headlines
Nice to have
• I'd like to see professional style brochure with squares integrated in.
Should not have
• VIBRANT COLORS

```html
<!DOCTYPE html>
<html lang="en">
<head>
<meta charset="utf-8">
<title>Shift Haven – On Call Service Brochure</title>
<link rel="stylesheet" href="https://fonts.googleapis.com/css2?family=Libre+Baskerville&family=Poppins:wght@400;500;600;700&display=swap">
<style>
:root{
  --navy:#1a4c7e;
  --navy-deep:#123a66;
  --navy-panel:#1b4d80;
  --slate:#7a7d82;
  --slate-blue:#7a8695;
  --mist:#cfd3d8;
  --ink:#1d1d1d;
  --grey-head:#5a5f66;
  --accent-blue:#1d5fa0;
  --badge:#2c6aa6;
  --paper:#ffffff;
  --stage:#a0a0a0;
}
*{box-sizing:border-box;margin:0;padding:0}
html,body{width:1200px;height:2901px;overflow:hidden;background:var(--stage)}
body{position:relative;font-family:"Poppins",sans-serif;color:var(--ink)}
.spread{position:absolute;left:85px;width:1030px;height:794px;background:var(--paper);overflow:hidden;box-shadow:0 2px 6px rgba(0,0,0,.15)}
.spread-outside{top:609px}
.spread-inside{top:1498px}
.abs{position:absolute}
.serif{font-family:"Libre Baskerville",serif;font-weight:400}
.photo{position:absolute;border:4px solid var(--paper)}
.body-copy{font-size:12.2px;line-height:14px;color:#222;letter-spacing:-.2px}
.blue-block{background:linear-gradient(180deg,var(--navy-panel),var(--navy-deep))}
.white{color:#fff}

/* outside spread */
.about-title{left:37px;top:30px;font-size:23px;color:var(--navy)}
.about-copy{left:37px;top:68px;width:262px}
.why-block{left:0;top:504px;width:348px;height:290px}
.why-title{left:39px;top:652px;font-size:23px}
.why-list{left:39px;top:694px;list-style:none;font-size:14.5px;line-height:24.5px}
.why-list li{display:flex;align-items:center;gap:6px}
.why-list svg{flex:none}
.tagline-block{left:365px;top:0;width:307px;height:281px;background:var(--slate)}
.tagline{left:365px;top:60px;width:307px;text-align:center;font-size:17px;line-height:20px;font-weight:500;color:#fff}
.brand-name{font-weight:700;color:var(--navy);letter-spacing:1.5px;text-align:center}
.brand-mid{left:365px;top:487px;width:307px;font-size:15px}
.contact-title{left:365px;top:518px;width:307px;text-align:center;font-size:16.5px;font-weight:600}
.contact{left:365px;width:307px;display:flex;flex-direction:column;align-items:center;gap:5px;font-size:11px}
.brand-right{left:690px;top:100px;width:340px;font-size:22px}
.frame-square{left:690px;top:138px;width:233px;height:250px;background:var(--navy)}
.oncall{left:726px;top:525px;font-size:43px;font-weight:600;color:var(--grey-head);line-height:46px}
.service{left:724px;top:570px;font-size:62px;font-weight:700;color:var(--navy);line-height:64px;letter-spacing:.5px}
.bar{left:728px;top:647px;width:4px;height:52px;background:var(--grey-head)}
.weekends{left:743px;top:639px;font-size:32px;line-height:33px;font-weight:600;color:var(--accent-blue)}
.web{left:690px;top:736px;width:340px;text-align:center;font-size:21px;font-weight:600;letter-spacing:2.5px}

/* inside spread */
.services-block{left:0;top:0;width:348px;height:529px}
.services-title{left:37px;top:50px;font-size:23px}
.service-item{position:absolute;left:37px;width:300px}
.service-pill{display:flex;align-items:center;gap:6px}
.pill{display:inline-block;width:150px;height:22px;border-radius:11px;background:#fff;color:var(--navy);font-size:12.5px;font-weight:600;line-height:22px;padding-left:12px}
.service-desc{margin-left:29px;margin-top:4px;font-size:12.3px;line-height:14px;color:#fff}
.square-grey{background:var(--slate-blue)}
.square-mist{background:var(--mist)}
.agency-title{left:386px;top:435px;font-size:23px;color:var(--navy)}
.agency-copy{left:386px;top:467px;width:252px}
.staff-block{left:690px;top:0;width:340px;height:512px}
.staff-title{left:728px;top:42px;font-size:24px;line-height:26px}
.staff-sub{left:728px;top:68px;width:280px;font-size:14.5px;line-height:17px;font-weight:600}
.badge{left:728px;top:101px;width:117px;height:32px;border-radius:16px;background:var(--badge);border:2px solid #fff;display:flex;align-items:center;gap:10px;padding-left:4px;color:#fff;font-weight:700;font-style:italic;font-size:21px}
.checks{left:738px;top:146px;list-style:none;font-size:12px;line-height:18px;font-weight:600}
.checks li{display:flex;align-items:center;gap:6px}
.empower-title{left:728px;top:226px;font-size:23px;line-height:24px}
.empower-copy{left:728px;top:290px;width:262px;font-size:12.2px;line-height:14px;letter-spacing:-.2px}
</style>
</head>
<body>

<section class="spread spread-outside" aria-label="Brochure outside panels">
  <h2 class="abs serif about-title">About us</h2>
  <p class="abs body-copy about-copy">Comprehensive on-call staffing solution designed for home care by home care professionals. Experience seamless scheduling tailored to meet the unique needs of your clients and staff Our team understands the demands of home care, ensuring that every shift is covered by qualified, compassionate caregivers. We prioritize flexibility and reliability, so you can focus on providing &nbsp;exceptional care while we handle the logistics Whether you need last-minute coverage or regular scheduling support, our service is here to enhance your operation's efficiency and peace of mind. Let us help you get your weekends back and maintain the high standards your clients deserve.</p>
  <div class="abs blue-block why-block"></div>
  <div class="photo" style="left:39px;top:349px;width:270px;height:259px;background:linear-gradient(160deg,#d9dbdd,#8a8f95 60%,#5c6066)" role="img" aria-label="Call center agents wearing headsets working at computer desks"></div>
  <h2 class="abs serif white why-title">Why Choose Us</h2>
  <ul class="abs white why-list">
    <li><svg width="16" height="16" viewBox="0 0 16 16"><circle cx="8" cy="8" r="7" fill="none" stroke="#fff" stroke-width="1.4"/><circle cx="8" cy="8" r="3" fill="#fff"/></svg>100% US Based</li>
    <li><svg width="16" height="16" viewBox="0 0 16 16"><circle cx="8" cy="8" r="7" fill="none" stroke="#fff" stroke-width="1.4"/><path d="M4 9 8 5l4 4v3H4z" fill="#fff"/></svg>Home care experts</li>
    <li><svg width="16" height="16" viewBox="0 0 16 16"><circle cx="8" cy="8" r="7" fill="none" stroke="#fff" stroke-width="1.4"/><path d="M5 8l2 2 4-4" fill="none" stroke="#fff" stroke-width="1.6"/></svg>Leading choice in on-call</li>
  </ul>

  <div class="abs tagline-block"></div>
  <p class="abs tagline">Home Care scheduling<br>by people who know<br>home care.</p>
  <div class="photo" style="left:388px;top:163px;width:261px;height:234px;background:linear-gradient(150deg,#e6e7e8,#9da3a8 55%,#3d4147)" role="img" aria-label="Smiling professional team seated around a meeting table"></div>
  <p class="abs brand-name brand-mid">SHIFT HAVEN</p>
  <h3 class="abs contact-title">Get In Touch With Us</h3>
  <div class="abs contact" style="top:553px">
    <svg width="24" height="24" viewBox="0 0 24 24"><circle cx="12" cy="12" r="12" fill="var(--navy)"/><path d="M8 6.5l2 .2.8 2.8-1.3 1a7 7 0 0 0 3.6 3.6l1-1.3 2.8.8.2 2a1.4 1.4 0 0 1-1.5 1.2A10 10 0 0 1 6.8 8a1.4 1.4 0 0 1 1.2-1.5z" fill="#fff"/></svg>
    <span>555.014.2290</span>
  </div>
  <div class="abs contact" style="top:608px">
    <svg width="24" height="24" viewBox="0 0 24 24"><circle cx="12" cy="12" r="12" fill="var(--navy)"/><rect x="6.5" y="8" width="11" height="8" fill="#fff"/><path d="M6.5 8 12 12.5 17.5 8" fill="none" stroke="var(--navy)" stroke-width="1.2"/></svg>
    <span>contact@shifthavenhq.com</span>
  </div>
  <div class="abs contact" style="top:663px">
    <svg width="24" height="24" viewBox="0 0 24 24"><circle cx="12" cy="12" r="12" fill="var(--navy)"/><path d="M12 5.5a4 4 0 0 1 4 4c0 3-4 8-4 8s-4-5-4-8a4 4 0 0 1 4-4z" fill="#fff"/><circle cx="12" cy="9.6" r="1.5" fill="var(--navy)"/></svg>
    <span>Cedar Point Texas</span>
  </div>
  <div class="abs contact" style="top:714px">
    <svg width="24" height="24" viewBox="0 0 24 24"><circle cx="12" cy="12" r="12" fill="var(--navy)"/><circle cx="12" cy="12" r="5.5" fill="none" stroke="#fff" stroke-width="1.3"/><path d="M6.5 12h11M12 6.5c-2.5 3-2.5 8 0 11M12 6.5c2.5 3 2.5 8 0 11" fill="none" stroke="#fff" stroke-width="1.1"/></svg>
    <span>www.shifthaven.com</span>
  </div>

  <p class="abs brand-name brand-right">SHIFT HAVEN</p>
  <div class="abs frame-square"></div>
  <div class="photo" style="left:724px;top:173px;width:273px;height:315px;border-width:0;background:linear-gradient(180deg,#e9e6e2 0%,#c9c3bb 45%,#8c7660 100%)" role="img" aria-label="Diverse group of caregivers standing in front of an American flag"></div>
  <p class="abs oncall">ON CALL</p>
  <p class="abs service">SERVICE</p>
  <div class="abs bar"></div>
  <p class="abs weekends">Get your<br>weekends back</p>
  <p class="abs web">www.shifthaven.com</p>
</section>

<section class="spread spread-inside" aria-label="Brochure inside panels">
  <div class="abs blue-block services-block"></div>
  <div class="abs square-grey" style="left:0;top:332px;width:216px;height:100px"></div>
  <div class="abs" style="left:0;top:366px;width:183px;height:163px;background:var(--navy-deep)"></div>
  <div class="abs square-mist" style="left:0;top:557px;width:40px;height:34px"></div>
  <h2 class="abs serif white services-title">Our Services</h2>
  <div class="service-item" style="top:80px">
    <div class="service-pill"><svg width="24" height="24" viewBox="0 0 24 24"><circle cx="12" cy="12" r="11" fill="none" stroke="#fff" stroke-width="1.5"/><circle cx="12" cy="12" r="4" fill="#fff"/></svg><span class="pill">ON-CALL STAFFING</span></div>
    <p class="service-desc">Our dedicated staffing teams<br>answer your calls and respond as<br>an extension of your agency</p>
  </div>
  <div class="service-item" style="top:162px">
    <div class="service-pill"><svg width="24" height="24" viewBox="0 0 24 24"><circle cx="12" cy="12" r="11" fill="none" stroke="#fff" stroke-width="1.5"/><circle cx="12" cy="10" r="3" fill="#fff"/><path d="M6.5 17a5.5 4 0 0 1 11 0z" fill="#fff"/></svg><span class="pill">RECRUITING</span></div>
    <p class="service-desc">Looking for the best caregivers?<br>Let Shift Haven find qualified<br>professionals for you.</p>
  </div>
  <div class="service-item" style="top:250px">
    <div class="service-pill"><svg width="24" height="24" viewBox="0 0 24 24"><circle cx="12" cy="12" r="11" fill="none" stroke="#fff" stroke-width="1.5"/><path d="M7.5 12l3 3 6-6" fill="none" stroke="#fff" stroke-width="1.8"/></svg><span class="pill">INTAKE</span></div>
    <p class="service-desc">Don't miss out with our intake services.</p>
  </div>
  <div class="photo" style="left:39px;top:414px;width:270px;height:340px;background:linear-gradient(160deg,#2d4f66,#1b3344 50%,#7a5a2a)" role="img" aria-label="Agent with headset working at a computer in a busy call center"></div>

  <div class="photo" style="left:386px;top:34px;width:266px;height:343px;border-width:0;background:linear-gradient(160deg,#dcdcd6,#8fa3a8 55%,#3a5966)" role="img" aria-label="Smiling professional shaking hands with a colleague in an office"></div>
  <h2 class="abs serif agency-title">Your Agency Matters</h2>
  <p class="abs body-copy agency-copy">You will benefit from dedicated implementation staff, along with the reassurance that your agency is our highest priority Our team is committed to understanding your unique needs and providing tailored solutions that enhance your agency's operations. From seamless onboarding to ongoing support, we ensure that every aspect of our service is designed to empower you and facilitate your success.With our expertise, you can focus on what truly matters delivering exceptional care to your clients. Whether you're expanding your services or streamlining existing processes, we're here to support you every step of the way. Let us help you elevate your agency to new heights,ensuring both your staff and clients &nbsp;experience the best possible outcomes.</p>

  <div class="abs blue-block staff-block"></div>
  <div class="abs square-grey" style="left:834px;top:360px;width:196px;height:152px"></div>
  <div class="abs" style="left:865px;top:390px;width:165px;height:122px;background:var(--navy-deep)"></div>
  <div class="abs square-mist" style="left:994px;top:585px;width:36px;height:29px"></div>
  <h2 class="abs serif white staff-title">US Based Staff</h2>
  <p class="abs white staff-sub">Shift Haven is supported by<br>U.S.-based agents available</p>
  <div class="abs badge">
    <svg width="24" height="24" viewBox="0 0 24 24"><circle cx="12" cy="12" r="12" fill="#fff"/><path d="M8 6.5l2 .2.8 2.8-1.3 1a7 7 0 0 0 3.6 3.6l1-1.3 2.8.8.2 2a1.4 1.4 0 0 1-1.5 1.2A10 10 0 0 1 6.8 8a1.4 1.4 0 0 1 1.2-1.5z" fill="var(--badge)"/></svg>
    <span>24/7</span>
  </div>
  <ul class="abs white checks">
    <li><svg width="10" height="10" viewBox="0 0 10 10"><circle cx="5" cy="5" r="5" fill="#fff"/><path d="M2.7 5.2l1.6 1.5 3-3" fill="none" stroke="var(--navy)" stroke-width="1.3"/></svg>Real people.</li>
    <li><svg width="10" height="10" viewBox="0 0 10 10"><circle cx="5" cy="5" r="5" fill="#fff"/><path d="M2.7 5.2l1.6 1.5 3-3" fill="none" stroke="var(--navy)" stroke-width="1.3"/></svg>Real assistance.</li>
    <li><svg width="10" height="10" viewBox="0 0 10 10"><circle cx="5" cy="5" r="5" fill="#fff"/><path d="M2.7 5.2l1.6 1.5 3-3" fill="none" stroke="var(--navy)" stroke-width="1.3"/></svg>Real growth. Every single time.</li>
  </ul>
  <h2 class="abs serif white empower-title">Empower Your<br>Agency for Expansion</h2>
  <p class="abs white empower-copy">Shift Haven is not just an answering service; we provide a comprehensive solution for after-hours coverage. Say goodbye to expensive overtime costs and the risk of staff burnout.</p>
  <div class="photo" style="left:728px;top:419px;width:262px;height:339px;background:linear-gradient(160deg,#e1e2e3,#8e9298 50%,#2b2e33)" role="img" aria-label="Manager guiding headset agents working at office computers"></div>
</section>

</body>
</html>
```